Design Hybrid Mobile App (React Native)

Design hybrid mobile app for both iOS and Android.

Application design should utilize React Native design libraries and elements, and should have all sufficient aspects of application features and functionalities to direct developer to fully develop an MVP, i.e. error/invalid/valid messages, all case scenarios... etc.

Design needs to be optimized for and follow latest Apple and Android device sizes and should be provided in Adobe Experience or Sketch design format, and all elements need to be vectors.

Designs need to be provided with free stock images, animations for page transitions need to be provided portray UX.

A full library of colors, buttons and design elements should be provided in one files as well. Future roadmap of design elements (style guide, including fonts and branding required).

Minimal text entry in design, use of modern form elements (e.g. sliders), modern look required.
Updates

Need extra days to review

Font styles to use
Sans Serif

Colors

Designer to choose colors to be used in the design.

Requirements
Must have
• Experience/UX built around it, not just buttons and screens

```html
<!DOCTYPE html>
<html lang="en">
<head>
<meta charset="utf-8">
<title>Platewise – App Screens</title>
<link rel="stylesheet" href="https://fonts.googleapis.com/css2?family=Inter:wght@300;400;500;600;700&display=swap">
<style>
  :root {
    --brand-blue: #3d5afe;
    --sky-blue: #1ab3f7;
    --orange: #ff8a1e;
    --orange-light: #ff9c2a;
    --ink: #222833;
    --ink-soft: #3a3f4a;
    --muted: #9aa0aa;
    --white: #ffffff;
    --paper: #ffffff;
    --field: rgba(255,255,255,0.22);
    --kbd-bg: #d2d5db;
    --kbd-key: #ffffff;
    --kbd-dark: #abb0ba;
    --badge: #ff3b30;
  }
  * { box-sizing: border-box; margin: 0; padding: 0; }
  html, body { width: 1200px; height: 1200px; overflow: hidden; background: var(--paper); }
  body { position: relative; font-family: "Inter", sans-serif; color: var(--ink); }

  .screen {
    position: absolute; width: 241px; height: 526px;
    border-radius: 26px; overflow: hidden; background: var(--white);
    box-shadow: 0 0 0 1px #e4e6ea;
  }
  .screen--welcome { left: 63px; top: 38px; }
  .screen--login   { left: 856px; top: 38px; }
  .screen--home    { left: 63px; top: 632px; }
  .screen--result  { left: 856px; top: 632px; }

  .backdrop {
    position: absolute; inset: 0;
    background: linear-gradient(180deg, #56555a 0%, #4a4a50 45%, #2a2c33 60%, #3b3b40 80%, #2c2e35 100%);
  }
  .app-name {
    position: absolute; left: 0; right: 0; text-align: center;
    color: var(--white); font-weight: 300; font-size: 17px;
  }
  .welcome-name { top: 218px; }
  .login-name { top: 182px; }

  .pill-btn {
    position: absolute; left: 30px; width: 182px; height: 30px; border-radius: 15px;
    display: flex; align-items: center; gap: 12px; padding-left: 10px;
    color: var(--white); font-size: 7.5px; font-weight: 600;
  }
  .pill-btn svg { width: 16px; height: 16px; }
  .pill-btn--foodies { top: 314px; background: linear-gradient(90deg, var(--orange), var(--orange-light)); }
  .pill-btn--restaurant { top: 366px; background: var(--sky-blue); }
  .create-bar {
    position: absolute; left: 0; right: 0; bottom: 0; height: 30px;
    background: var(--brand-blue); color: var(--white);
    display: flex; align-items: center; justify-content: center;
    font-size: 7.5px; font-weight: 600;
  }

  .login-title { position: absolute; left: 29px; top: 222px; color: var(--white); font-size: 16px; font-weight: 300; }
  .field {
    position: absolute; left: 30px; width: 181px; height: 30px; border-radius: 15px;
    background: var(--field); display: flex; align-items: center; gap: 10px; padding-left: 12px;
    color: var(--white); font-size: 7.5px; font-weight: 600;
  }
  .field svg { width: 12px; height: 12px; }
  .field--email { top: 260px; }
  .field--password { top: 312px; }

  .keyboard {
    position: absolute; left: 0; right: 0; bottom: 0; height: 140px; background: var(--kbd-bg);
    padding: 6px 2px 0; display: flex; flex-direction: column; gap: 6px;
  }
  .kbd-row { display: flex; justify-content: center; gap: 4px; }
  .key {
    width: 20px; height: 28px; border-radius: 4px; background: var(--kbd-key);
    box-shadow: 0 1px 0 #8d919a; display: flex; align-items: center; justify-content: center;
    font-size: 14px; font-weight: 300; color: #222;
  }
  .key svg { width: 11px; height: 11px; }
  .key--dark { background: var(--kbd-dark); width: 27px; font-size: 10px; }
  .key--space { flex: 0 0 96px; font-size: 10px; }
  .key--return { width: 56px; background: var(--kbd-dark); font-size: 10px; }

  .search {
    position: absolute; left: 40px; top: 28px; width: 160px; height: 24px; border-radius: 12px;
    background: var(--white); box-shadow: 0 2px 6px rgba(0,0,0,0.08);
    display: flex; align-items: center; gap: 7px; padding-left: 10px;
    font-size: 6.5px; color: var(--muted);
  }
  .search svg { width: 8px; height: 8px; }
  .avatar { position: absolute; left: 207px; top: 30px; width: 20px; height: 20px; border-radius: 50%; background: #c94646; box-shadow: 0 0 0 1.5px #e6e7ea; }

  .section-label { position: absolute; left: 14px; font-size: 7.5px; font-weight: 600; color: var(--ink-soft); }

  .tile { position: absolute; overflow: hidden; }
  .tile .photo { position: absolute; inset: 0; }
  .tile .tile-name {
    position: absolute; left: 9px; bottom: 4px; color: var(--white);
    font-size: 10.5px; font-weight: 700; text-shadow: 0 1px 2px rgba(0,0,0,0.45);
  }
  .fade { position: absolute; left: 0; right: 0; top: 420px; height: 80px; background: linear-gradient(180deg, rgba(255,255,255,0) 0%, #fff 80%); }

  .tab-bar { position: absolute; left: 0; right: 0; bottom: 12px; display: flex; justify-content: space-around; padding: 0 16px; }
  .tab-bar svg { width: 14px; height: 14px; }

  .not-quite { position: absolute; left: 0; right: 0; top: 298px; text-align: center; font-size: 7.5px; font-weight: 600; color: var(--ink-soft); }
  .submit-btn {
    position: absolute; left: 46px; top: 318px; width: 148px; height: 25px; border-radius: 13px;
    background: var(--brand-blue); color: var(--white); font-size: 7.5px; font-weight: 600;
    display: flex; align-items: center; justify-content: center; white-space: nowrap;
  }

  .brand-mark { position: absolute; left: 426px; top: 300px; width: 300px; height: 300px; border-radius: 50%; background: var(--brand-blue); }
  .brand-name { position: absolute; left: 400px; top: 712px; width: 352px; text-align: center; font-size: 62px; font-weight: 400; color: var(--brand-blue); letter-spacing: -1px; }
  .brand-copy { position: absolute; left: 399px; top: 828px; width: 372px; font-size: 5.2px; line-height: 8px; font-weight: 700; color: #111; }
</style>
</head>
<body>

  <!-- Welcome screen -->
  <section class="screen screen--welcome">
    <div class="backdrop" role="img" aria-label="Blurred restaurant interior photo in dark grey tones"></div>
    <div class="app-name welcome-name">Platewise</div>
    <div class="pill-btn pill-btn--foodies">
      <svg viewBox="0 0 16 16" fill="none" stroke="#fff" stroke-width="1"><path d="M4 9a3 3 0 0 1 1-5.5 3 3 0 0 1 6 0A3 3 0 0 1 12 9v4H4z"/><path d="M4 11h8"/></svg>
      Log in Foodies
    </div>
    <div class="pill-btn pill-btn--restaurant">
      <svg viewBox="0 0 16 16" fill="none" stroke="#fff" stroke-width="1"><path d="M2 7a6 4 0 0 1 12 0z"/><path d="M2 9h12M2 11h12"/><path d="M3 11v1.5h10V11"/></svg>
      Log in Restaurant
    </div>
    <div class="create-bar">Create your account</div>
  </section>

  <!-- Login screen -->
  <section class="screen screen--login">
    <div class="backdrop" role="img" aria-label="Blurred restaurant interior photo in dark grey tones"></div>
    <div class="app-name login-name">Platewise</div>
    <h1 class="login-title">Log in</h1>
    <div class="field field--email">
      <svg viewBox="0 0 12 12" fill="none" stroke="#fff" stroke-width="1"><rect x="1" y="2.5" width="10" height="7"/><path d="M1 2.5l5 4 5-4"/></svg>
      Email Address
    </div>
    <div class="field field--password">
      <svg viewBox="0 0 12 12" fill="none" stroke="#fff" stroke-width="1"><rect x="2.5" y="5.5" width="7" height="6"/><path d="M4 5.5V3.5a2 2 0 0 1 4 0v2"/></svg>
      Password
    </div>
    <div class="keyboard">
      <div class="kbd-row"><span class="key">q</span><span class="key">w</span><span class="key">e</span><span class="key">r</span><span class="key">t</span><span class="key">y</span><span class="key">u</span><span class="key">i</span><span class="key">o</span><span class="key">p</span></div>
      <div class="kbd-row"><span class="key">a</span><span class="key">s</span><span class="key">d</span><span class="key">f</span><span class="key">g</span><span class="key">h</span><span class="key">j</span><span class="key">k</span><span class="key">l</span></div>
      <div class="kbd-row"><span class="key key--dark">⇧</span><span class="key">z</span><span class="key">x</span><span class="key">c</span><span class="key">v</span><span class="key">b</span><span class="key">n</span><span class="key">m</span><span class="key key--dark">⌫</span></div>
      <div class="kbd-row">
        <span class="key key--dark">123</span>
        <span class="key key--dark"><svg viewBox="0 0 12 12" fill="none" stroke="#333" stroke-width="0.9"><circle cx="6" cy="6" r="4.8"/><path d="M3.8 7.2a2.6 2.6 0 0 0 4.4 0"/><circle cx="4.4" cy="4.8" r="0.5" fill="#333"/><circle cx="7.6" cy="4.8" r="0.5" fill="#333"/></svg></span>
        <span class="key"><svg viewBox="0 0 12 12" fill="none" stroke="#333" stroke-width="0.9"><rect x="4.3" y="1" width="3.4" height="6" rx="1.7"/><path d="M2.8 5.5a3.2 3.2 0 0 0 6.4 0M6 8.7V11"/></svg></span>
        <span class="key key--space">space</span>
        <span class="key key--return">return</span>
      </div>
    </div>
  </section>

  <!-- Home / discover screen -->
  <section class="screen screen--home">
    <div class="search">
      <svg viewBox="0 0 8 8" fill="none" stroke="#8a9099" stroke-width="0.9"><circle cx="3.3" cy="3.3" r="2.5"/><path d="M5.2 5.2L7.5 7.5"/></svg>
      Search Platewise
    </div>
    <div class="avatar"></div>
    <div class="section-label" style="top:82px">Most Popular in KSA</div>
    <div class="tile" style="left:14px;top:98px;width:108px;height:62px">
      <div class="photo" role="img" aria-label="Photo of toast with boiled eggs and greens" style="background:linear-gradient(135deg,#6b7a3e,#d9a24a 55%,#4f3a22)"></div>
      <span class="tile-name">Mezzah Night</span>
    </div>
    <div class="tile" style="left:134px;top:98px;width:97px;height:62px">
      <div class="photo" role="img" aria-label="Photo of a salad plate on a dark table" style="background:linear-gradient(135deg,#3a2a22,#b8605a 50%,#2c2a28)"></div>
      <span class="tile-name">Salad Guy</span>
    </div>
    <div class="tile" style="left:14px;top:172px;width:217px;height:146px">
      <div class="photo" role="img" aria-label="Photo of grilled chicken and vegetable skewers" style="background:linear-gradient(150deg,#2a2e38,#c7b04a 35%,#6b5a3a 60%,#2b2f35)"></div>
      <span class="tile-name">Maxican Dip Devil</span>
    </div>
    <div class="section-label" style="top:350px">Introducing</div>
    <div class="tile" style="left:14px;top:366px;width:102px;height:57px">
      <div class="photo" role="img" aria-label="Photo of a curry dish in a white bowl" style="background:linear-gradient(135deg,#d8cfc6,#9a4a30 55%,#5a3a2a)"></div>
      <span class="tile-name">Indian Mama</span>
    </div>
    <div class="tile" style="left:129px;top:366px;width:102px;height:57px">
      <div class="photo" role="img" aria-label="Photo of flatbreads and dips on a table" style="background:linear-gradient(135deg,#3a3a3a,#c9a46a 50%,#2e2a26)"></div>
      <span class="tile-name">Zina King</span>
    </div>
    <div class="tile" style="left:14px;top:436px;width:146px;height:50px">
      <div class="photo" role="img" aria-label="Photo of a seafood dish" style="background:linear-gradient(135deg,#e9c9bb,#d98a6a)"></div>
    </div>
    <div class="tile" style="left:172px;top:436px;width:59px;height:50px">
      <div class="photo" role="img" aria-label="Photo of a plated meal" style="background:linear-gradient(135deg,#3a3f4a,#8a6a5a)"></div>
    </div>
    <div class="fade"></div>
    <nav class="tab-bar">
      <svg viewBox="0 0 14 14" fill="none" stroke="#3d5afe" stroke-width="1"><path d="M2 6.5L7 2l5 4.5V12H2z"/><path d="M5.5 12V8.5h3V12"/></svg>
      <svg viewBox="0 0 14 14" fill="none" stroke="#3a3f4a" stroke-width="1"><path d="M1 2.5h2l1.5 6.5h7l1-4.5H4"/><circle cx="5.5" cy="11.5" r="1"/><circle cx="10.5" cy="11.5" r="1"/><circle cx="3" cy="2" r="1.8" fill="#ff3b30" stroke="none"/></svg>
      <svg viewBox="0 0 14 14" fill="none" stroke="#3a3f4a" stroke-width="1"><path d="M1.5 2.5h11v7H7l-3 2.5v-2.5H1.5z"/></svg>
      <svg viewBox="0 0 14 14" fill="none" stroke="#3a3f4a" stroke-width="1"><circle cx="7" cy="4.5" r="2.8"/><path d="M1.5 13c.5-3 2.8-4.5 5.5-4.5s5 1.5 5.5 4.5z"/></svg>
    </nav>
  </section>

  <!-- Search result screen -->
  <section class="screen screen--result">
    <div class="search">
      <svg viewBox="0 0 8 8" fill="none" stroke="#8a9099" stroke-width="0.9"><circle cx="3.3" cy="3.3" r="2.5"/><path d="M5.2 5.2L7.5 7.5"/></svg>
      Steak
    </div>
    <div class="avatar"></div>
    <div class="section-label" style="top:82px">Fancy this?</div>
    <div class="tile" style="left:14px;top:98px;width:217px;height:101px">
      <div class="photo" role="img" aria-label="Photo of salmon steaks on a white plate" style="background:radial-gradient(ellipse at 65% 50%,#f29a6a 0%,#e57a4e 30%,#2a2320 75%)"></div>
      <span class="tile-name">Freak Steak</span>
    </div>
    <div class="not-quite">Not Quite...</div>
    <div class="submit-btn">Submit your Platewise Request</div>
    <nav class="tab-bar">
      <svg viewBox="0 0 14 14" fill="none" stroke="#3d5afe" stroke-width="1"><path d="M2 6.5L7 2l5 4.5V12H2z"/><path d="M5.5 12V8.5h3V12"/></svg>
      <svg viewBox="0 0 14 14" fill="none" stroke="#3a3f4a" stroke-width="1"><path d="M1 2.5h2l1.5 6.5h7l1-4.5H4"/><circle cx="5.5" cy="11.5" r="1"/><circle cx="10.5" cy="11.5" r="1"/><circle cx="3" cy="2" r="1.8" fill="#ff3b30" stroke="none"/></svg>
      <svg viewBox="0 0 14 14" fill="none" stroke="#3a3f4a" stroke-width="1"><path d="M1.5 2.5h11v7H7l-3 2.5v-2.5H1.5z"/></svg>
      <svg viewBox="0 0 14 14" fill="none" stroke="#3a3f4a" stroke-width="1"><circle cx="7" cy="4.5" r="2.8"/><path d="M1.5 13c.5-3 2.8-4.5 5.5-4.5s5 1.5 5.5 4.5z"/></svg>
    </nav>
  </section>

  <!-- Brand block -->
  <div class="brand-mark"></div>
  <div class="brand-name">Platewise</div>
  <p class="brand-copy">Platewise helps hungry people find the right dish without typing much. Browse what is popular near you, save the places you love and tell us what you crave. Restaurants join in minutes, add their menus and reach new diners every day. Our clear colours, soft shapes and large photos keep each step simple, whether you order, reserve a table or share a review. Smooth transitions guide you from one screen to the next, and friendly messages explain every error or success. Built for iOS and Android with one shared codebase, the app grows with a full style guide, reusable components and a roadmap for new features.</p>

</body>
</html>
```